Menu Design Project for new restauranct concept

Design menu for new restaurant concept called Juniper's Burgers & Dogs. Logo is attached.

Industry/Entity Type

Restaurant

Requirements
Must have
• Menu items and pricing:

Burgers
Snack Burger $3.49
Snack Cheeseburger $3.99
Juniper's signature Burger $4.99
Juniper's signature Cheeseburger $5.49
Burger toppings: bacon, lettuce, tomato, onion, pickle, grilled onions, grilled mushrooms, grilled green peppers, jalapeƱo peppers.

Dogs
Hot Dog $2.99
Bacon Cheese Hot Dog $3.99
Slaw Dog $3.99
Kraut Dog $3.49
Chili Dog $3.99 with or with out cheese
Hot dogs are 100% beef

Other
Grilled Chicken Sandwich $5.99
Grilled Chicken Sandwich with cheese $6.49
(Same toppings as burgers)

French Fries $1.99

Loaded Potatos
The Plain Tater: $4.99 choose from: butter, sour cream, cheese, chives
The Garden Tater: $5.99 choose from: the Basic plus, broccoli & cheese, grilled mushrooms, onions, & peppers
The Rancher Tater: $6.99 choose from the Basic/Veggie plus: grilled chicken, chili, Philly cheesesteak, pulled pork.

Drinks
32oz. Drink $1.88
20oz. Drink $1.69

attached logo.
Nice to have
• love to incorporate the woodgrain backgound. It makes the logo look most like a cattle brand, which we like.

```html
<!DOCTYPE html>
<html lang="en">
<head>
<meta charset="utf-8">
<title>Juniper's Burgers &amp; Dogs — Menu</title>
<link href="https://fonts.googleapis.com/css2?family=Stardos+Stencil:wght@700&family=Pathway+Gothic+One&display=swap" rel="stylesheet">
<style>
:root{
  --ink:#111;
  --muted:#444;
  --banner:#000;
  --title:#d2d2d2;
  --wood-light:#d9d7d2;
  --wood-mid:#a9a6a0;
  --wood-dark:#6f6b66;
  --paper:#fff;
  --watermark:#e4e4e4;
}
*{margin:0;padding:0;box-sizing:border-box}
html,body{width:927px;height:1200px;overflow:hidden;background:var(--paper)}
.menu{position:relative;width:927px;height:1200px;overflow:hidden;background:var(--paper);
  font-family:"Pathway Gothic One",sans-serif;color:var(--ink)}
.wood{position:absolute;left:0;top:0;width:927px;height:345px;
  background:
    repeating-linear-gradient(90deg,rgba(0,0,0,.10) 0 3px,transparent 3px 104px),
    linear-gradient(90deg,var(--wood-mid),var(--wood-light) 20%,var(--wood-mid) 40%,var(--wood-light) 60%,var(--wood-dark) 80%,var(--wood-light));
  -webkit-mask-image:linear-gradient(180deg,#000 0,#000 250px,transparent 345px);
          mask-image:linear-gradient(180deg,#000 0,#000 250px,transparent 345px)}
.watermark{position:absolute;left:190px;top:370px;width:880px;height:880px}
.banner{position:absolute;left:139px;top:57px;width:788px;height:195px;background:var(--banner)}
.brand{position:absolute;left:156px;top:59px;width:192px;height:192px;border-radius:50%;
  background:var(--wood-light);display:flex;align-items:center;justify-content:center;
  font-family:"Stardos Stencil",sans-serif;font-weight:700;font-size:38px;color:var(--ink)}
.title{position:absolute;left:425px;top:130px;font-family:"Stardos Stencil",sans-serif;font-weight:700;
  font-size:46px;line-height:56px;color:var(--title);letter-spacing:.5px}
.line{position:absolute;left:187px;white-space:nowrap;font-size:15.5px;line-height:20px}
.heading{position:absolute;left:187px;font-family:"Stardos Stencil",sans-serif;font-weight:700;
  font-size:22px;line-height:26px;color:var(--ink);letter-spacing:.5px}
.note{position:absolute;left:187px;font-size:12.5px;line-height:15px;color:var(--muted);white-space:nowrap}
.note b{font-weight:400;color:var(--ink);font-size:13.5px}
.note.small{font-size:10.5px;font-style:italic}
.price{position:absolute;left:351px;font-size:15.5px;line-height:20px}
.price.near{left:297px}
.price.shift{left:355px}
</style>
</head>
<body>
<main class="menu">
  <div class="wood" role="img" aria-label="Weathered grey wooden planks fading into white"></div>

  <svg class="watermark" viewBox="0 0 880 880" aria-hidden="true">
    <circle cx="440" cy="440" r="420" fill="none" stroke="var(--watermark)" stroke-width="22"/>
    <text x="440" y="500" text-anchor="middle" font-family="Stardos Stencil, sans-serif" font-weight="700" font-size="150" fill="var(--watermark)">Juniper's</text>
  </svg>

  <div class="banner"></div>
  <div class="brand">Juniper's</div>
  <h1 class="title">BURGERS &amp; DOGS</h1>

  <h2 class="heading" style="top:323px">BURGERS</h2>
  <p class="note" style="top:350px"><b>Burger toppings:</b> bacon, lettuce, tomato, onion, pickle, grilled onions,</p>
  <p class="note" style="top:364px">grilled mushrooms, grilled green peppers, jalapeño peppers.</p>
  <p class="line" style="top:392px">Snack Burger</p><p class="price" style="top:392px">$3.49</p>
  <p class="line" style="top:414px">Snack Cheeseburger</p><p class="price" style="top:414px">$3.99</p>
  <p class="line" style="top:435px">Juniper's Signature Burger</p><p class="price" style="top:435px">$4.99</p>
  <p class="line" style="top:456px">Juniper's Signature Cheeseburger</p><p class="price shift" style="top:456px">$5.49</p>

  <h2 class="heading" style="top:503px">DOGS</h2>
  <p class="note" style="top:529px">Hot dogs are 100% beef</p>
  <p class="line" style="top:556px">Hot Dog</p><p class="price" style="top:556px">$2.99</p>
  <p class="line" style="top:577px">Bacon Cheese Hot Dog</p><p class="price" style="top:577px">$3.99</p>
  <p class="line" style="top:599px">Slaw Dog</p><p class="price" style="top:599px">$3.99</p>
  <p class="line" style="top:620px">Kraut Dog</p><p class="price" style="top:620px">$3.49</p>
  <p class="line" style="top:641px">Chili Dog</p><p class="price" style="top:641px">$3.99</p>
  <p class="note small" style="top:659px">with or without cheese</p>

  <h2 class="heading" style="top:696px">CHICKEN</h2>
  <p class="note" style="top:717px">(Same toppings as burgers)</p>
  <p class="line" style="top:746px">Grilled Chicken Sandwich</p><p class="price" style="top:746px">$5.99</p>
  <p class="line" style="top:767px">Grilled Chicken Sandwich</p><p class="price shift" style="top:767px">$6.49</p>
  <p class="note small" style="top:785px">with cheese</p>

  <h2 class="heading" style="top:818px">LOADED POTATOES</h2>
  <p class="line" style="top:855px">The Plain Tater</p><p class="price" style="top:855px">$4.99</p>
  <p class="note" style="top:872px">choose from: butter, sour cream, cheese, chives</p>
  <p class="line" style="top:893px">The Garden Tater</p><p class="price" style="top:893px">$5.99</p>
  <p class="note" style="top:911px">choose from: the Basic + broccoli &amp; cheese, grilled mushrooms, onions, peppers</p>
  <p class="line" style="top:933px">The Rancher Tater</p><p class="price" style="top:933px">$6.99</p>
  <p class="note" style="top:951px">choose from: the Basic/Veggie + grilled chicken, chili, Philly cheesesteak, pulled pork</p>

  <p class="line" style="top:996px">French Fries</p><p class="price near" style="top:996px">$1.99</p>

  <h2 class="heading" style="top:1043px">DRINKS</h2>
  <p class="line" style="top:1078px">20oz. drink</p><p class="price near" style="top:1078px">$1.69</p>
  <p class="line" style="top:1099px">32oz. drink</p><p class="price near" style="top:1099px">$1.88</p>
</main>
</body>
</html>
```